Fixed price car insurance banner ad for insurance broker

We need a banner ad for addition to web pages and which will advertise an innovative insurance product we are selling.

We are an insurance broker and our product is a fixed price car insurance product.

The banner ad needs to display the company logo. This will be uploaded within the file upload section.

The remainder of the banner ad needs to explain what we are offering and also include the gear stick picture for impact.

We would like to see colours that tie in with the corporate colours, or alternative are striking and have presence on even the busiest web page I.e. Black banner and silver / white text. Please see the file upload for a sample of the brochure we are preparing for this product.

Target Market(s)

Private and commercial clients with both regular and high value motor vehicles.

Industry/Entity Type

Car Insurance

Font styles to use
Serif
Sans Serif

Colors

Designer to choose colors to be used in the design.

Requirements
Must have
• The banner must have the company logo on both pages.

I would like the advert to scroll / roll / fade or other between two pages displaying the following text:

Page 1
"Motor Insurance Scheme"
"Anything But Standard"
and including the gear knob picture

Page 2
Any Driver, Any Car, No Forms and One Flat Premium*

On clicking the banner ad, this will open an email, pre populated with email contact to request more detail.

Nice to have
• Open to your suggestions on this
Should not have
• Nothing at this stage. I will guide you when the ads are being submitted.

```html
<!DOCTYPE html>
<html lang="en">
<head>
<meta charset="utf-8">
<title>Motor Insurance Scheme Banner</title>
<link href="https://fonts.googleapis.com/css2?family=PT+Sans:ital,wght@0,400;0,700;1,700&family=Cormorant+Garamond:wght@500&display=swap" rel="stylesheet">
<style>
  :root {
    --page-bg: #1b1b1b;
    --page-bg-light: #262626;
    --navy-deep: #16215a;
    --navy-mid: #25377f;
    --frame: #b9bcc4;
    --panel-light: #f7f7f8;
    --panel-shade: #dcdde0;
    --white: #ffffff;
    --accent: #f5a21b;
    --button: #ee5a12;
    --button-dark: #d34806;
    --logo-ink: #1f2f6e;
    --knob-light: #c9ccd2;
    --knob-dark: #3a3d44;
  }
  * { margin: 0; padding: 0; box-sizing: border-box; }
  html, body {
    width: 1200px; height: 336px; overflow: hidden;
    background: radial-gradient(ellipse at center, var(--page-bg-light), var(--page-bg) 75%);
  }
  .banner {
    position: absolute; left: 90px; top: 113px;
    width: 1010px; height: 127px;
    border: 1px solid var(--frame); border-radius: 7px;
    overflow: hidden; display: flex;
    font-family: "PT Sans", Arial, sans-serif;
  }
  .offer {
    position: relative; width: 817px; height: 100%;
    background: radial-gradient(ellipse 60% 120% at 62% 50%, var(--navy-mid), var(--navy-deep));
  }
  .gear-photo {
    position: absolute; left: 0; top: 0; width: 240px; height: 100%;
    background: radial-gradient(ellipse 55% 80% at 48% 55%, var(--knob-light), #8e929a 55%, var(--knob-dark) 85%, var(--navy-deep));
  }
  .copy {
    position: absolute; left: 250px; right: 20px; top: 0; height: 100%;
    display: flex; flex-direction: column; align-items: center; justify-content: center;
    color: var(--white); text-align: center;
  }
  .headline {
    font-size: 31px; font-weight: 700; font-style: italic; line-height: 1.05;
    letter-spacing: 0.2px; text-transform: uppercase;
  }
  .subline { font-size: 24px; font-weight: 700; line-height: 1.3; }
  .subline .highlight { color: var(--accent); }
  .details { font-size: 16px; line-height: 1.5; margin-top: 2px; }
  .pointer {
    position: absolute; left: 817px; top: 54px; width: 12px; height: 20px; z-index: 2;
  }
  .brand-panel {
    flex: 1; height: 100%;
    background: linear-gradient(180deg, var(--panel-light), var(--panel-shade));
    display: flex; flex-direction: column; align-items: center; justify-content: center; gap: 16px;
    padding-top: 4px;
  }
  .brand-name {
    font-family: "Cormorant Garamond", Georgia, serif; font-weight: 500;
    font-size: 22px; color: var(--logo-ink); letter-spacing: 1px; line-height: 1;
  }
  .cta {
    display: inline-flex; align-items: center; gap: 8px;
    width: 148px; height: 32px; justify-content: center;
    border-radius: 9px; text-decoration: none;
    background: linear-gradient(180deg, var(--button), var(--button-dark));
    color: var(--white); font-weight: 700; font-size: 17px;
  }
  .cta svg { width: 8px; height: 10px; }
</style>
</head>
<body>
  <a class="banner" href="mailto:info@harlowinsurance.example?subject=Motor%20Insurance%20Scheme" aria-label="Harlow Insurance motor insurance scheme">
    <div class="offer">
      <div class="gear-photo" role="img" aria-label="Close-up photograph of a chrome gear stick knob with shift pattern"></div>
      <div class="copy">
        <p class="headline">A Motor Insurance Scheme</p>
        <p class="subline">That’s <span class="highlight">Anything</span> But Standard</p>
        <p class="details">Any Driver, Any Car, No Forms and One Flat Premium*</p>
      </div>
    </div>
    <svg class="pointer" viewBox="0 0 12 20" aria-hidden="true"><polygon points="0,0 12,10 0,20" fill="#1d2b66"/></svg>
    <div class="brand-panel">
      <span class="brand-name">Harlow Insurance</span>
      <span class="cta">Learn More
        <svg viewBox="0 0 8 10" aria-hidden="true"><polygon points="0,0 8,5 0,10" fill="#ffffff"/></svg>
      </span>
    </div>
  </a>
</body>
</html>
```